Pet business needs a business card

Pet shop needs a business card. Like dark background and and debased look.

Meadowpaws
Lindenweg 47
B - 3280 Velmor
Belgium

www.meadowpaws-example.com
mail@meadowpaws-example.com
Phone +32478610927

I will ad a tagline shortly.

Industry/Entity Type

Shop

Font styles to use
Sans Serif

Requirements
Must have
• Must be possible to print the card debased. See example image.

```html
<!DOCTYPE html>
<html lang="en">
<head>
<meta charset="utf-8">
<title>Meadowpaws – Business Card</title>
<link rel="stylesheet" href="https://fonts.googleapis.com/css2?family=Roboto+Condensed:wght@400;700&display=swap">
<style>
  :root {
    --page: #ecebe8;
    --card-dark: #262a31;
    --kraft: #c4945c;
    --kraft-deep: #b5844d;
    --accent: #f7a236;
    --ink: #22252b;
    --shadow: rgba(0, 0, 0, 0.18);
  }
  * { box-sizing: border-box; margin: 0; padding: 0; }
  html, body {
    width: 1200px;
    height: 1024px;
    overflow: hidden;
    background: var(--page);
  }
  .canvas {
    width: 1200px;
    height: 1024px;
    display: flex;
    flex-direction: column;
    align-items: center;
    justify-content: center;
    gap: 60px;
  }
  .card {
    width: 760px;
    height: 434px;
    border-radius: 6px;
    box-shadow: 0 6px 18px var(--shadow);
    position: relative;
    overflow: hidden;
  }

  /* Front */
  .card-front {
    background: var(--card-dark);
    display: flex;
    align-items: center;
    justify-content: center;
    gap: 22px;
  }
  .brand-dot {
    width: 34px;
    height: 34px;
    border-radius: 50%;
    background: var(--accent);
  }
  .brand-name {
    font-family: "Roboto Condensed", sans-serif;
    font-weight: 700;
    font-size: 84px;
    letter-spacing: -1px;
    color: var(--accent);
    text-transform: lowercase;
    line-height: 1;
  }

  /* Back */
  .card-back {
    background: linear-gradient(135deg, var(--kraft) 0%, var(--kraft-deep) 100%);
    display: flex;
    align-items: center;
    padding: 0 48px 0 0;
  }
  .brand-panel {
    width: 330px;
    height: 100%;
    background: var(--card-dark);
    display: flex;
    align-items: center;
    justify-content: center;
    gap: 12px;
  }
  .brand-panel .brand-name { font-size: 48px; }
  .brand-panel .brand-dot { width: 20px; height: 20px; }

  .contact-list {
    list-style: none;
    margin-left: 48px;
    display: flex;
    flex-direction: column;
    gap: 20px;
    font-family: "Roboto Condensed", sans-serif;
    font-size: 20px;
    color: var(--ink);
  }
  .contact-item {
    display: flex;
    align-items: flex-start;
    gap: 16px;
  }
  .contact-icon {
    width: 26px;
    height: 26px;
    flex: none;
    border-radius: 5px;
    background: var(--ink);
    display: flex;
    align-items: center;
    justify-content: center;
  }
  .contact-icon svg { width: 16px; height: 16px; }
  .contact-text { line-height: 1.3; }
</style>
</head>
<body>
  <main class="canvas">
    <section class="card card-front" aria-label="Business card front">
      <span class="brand-dot" aria-hidden="true"></span>
      <h1 class="brand-name">meadowpaws</h1>
    </section>

    <section class="card card-back" aria-label="Business card back">
      <div class="brand-panel">
        <span class="brand-dot" aria-hidden="true"></span>
        <span class="brand-name">meadowpaws</span>
      </div>
      <ul class="contact-list">
        <li class="contact-item">
          <span class="contact-icon" aria-hidden="true">
            <svg viewBox="0 0 16 16"><path d="M4 2l2.5 3-1.5 1.5c.8 1.8 2.2 3.2 4 4L10.5 9 13.5 11.5 12 14C7 14 2 9 2 4z" fill="var(--accent)"/></svg>
          </span>
          <span class="contact-text">+32478610927</span>
        </li>
        <li class="contact-item">
          <span class="contact-icon" aria-hidden="true">
            <svg viewBox="0 0 16 16"><rect x="2" y="4" width="12" height="8" rx="1" fill="none" stroke="var(--accent)" stroke-width="1.5"/><path d="M2.5 4.5L8 9l5.5-4.5" fill="none" stroke="var(--accent)" stroke-width="1.5"/></svg>
          </span>
          <span class="contact-text">mail@meadowpaws-example.com</span>
        </li>
        <li class="contact-item">
          <span class="contact-icon" aria-hidden="true">
            <svg viewBox="0 0 16 16"><circle cx="8" cy="8" r="5.5" fill="none" stroke="var(--accent)" stroke-width="1.4"/><ellipse cx="8" cy="8" rx="2.3" ry="5.5" fill="none" stroke="var(--accent)" stroke-width="1.2"/><path d="M2.5 8h11" stroke="var(--accent)" stroke-width="1.2"/></svg>
          </span>
          <span class="contact-text">www.meadowpaws-example.com</span>
        </li>
        <li class="contact-item">
          <span class="contact-icon" aria-hidden="true">
            <svg viewBox="0 0 16 16"><path d="M8 15s-4.5-5-4.5-8.2a4.5 4.5 0 0 1 9 0C12.5 10 8 15 8 15z" fill="var(--accent)"/><circle cx="8" cy="6.8" r="1.6" fill="var(--ink)"/></svg>
          </span>
          <span class="contact-text">Lindenweg 47<br>B - 3280 Velmor, Belgium</span>
        </li>
      </ul>
    </section>
  </main>
</body>
</html>
```